Poster for company's 5 NORMS

Good Day,

My name is Rilo and I am working for Karvell & Brodick Maritime Pte Ltd. We are in the Marine and Offshore industry and based in Singapore.

I have to submit a few A-2 sized poster design samples reflecting our 5 norms to my boss in 40 hours time. So I need your help.

The 5 norms are: (1) Ownership, (2) Positive Mindset, (3) Actions, (4) Teamwork, (5) Honesty.

My company logo can be googled. The corporate colours of the company are blue and grey predominantly and white is occasionally used. But feel free to play with colours. No need to stick to grey, blue and white. The words and headers, you can play with colours too. This poster must be an attention grabber. You can make it look professional yet fun as well.

A few of the poster designs should be build based on the following:
a) 2 liner headers reading the following:
Line 1: Our Winning 5 Norms!
LIne 2: OWNing the P.A.T.H to Tier 1

b) Bottom centre - company's logo

c) Design 1: A winding road (limit to 2 turns) as background and the 5 norms spread vertically along the winding road.

d) Design 2: A circle divided into 5 equal segments and in each segment, the 5 norms.

You should consider highlighting for the initial letter (s) of each word (OWN, P, A, T, H) so that it will reemphasize Owning the Path. Also, attached is a design for the poster that we have on our walls now. I did not scan it properly but I would want a much much better poster.

Please feel free to be creative, especially for the other designs.

Thank you very much. Looking forward to see posters in my inbox.

Have a great day ahead,

Regards, Rilo

Hp: 65-91357248

Good Day,

I just attached a picture of our current poster. I did not scan it well, apologies for that. But we would want a much much better poster.

Thank you!

Hello guys,

I have attached a picture of the company's logo. You can also visit the link below to get the correct logo.

It should state "Karvell & Brodick Maritime".

Thanks.

https://www.searchbox-example.sg/find?q=karvell+and+brodick+maritime+logo

Target Market(s)

Internal stakeholders. Good if it can impress clients as well.

Industry/Entity Type

Industry

Font styles to use
Serif

```html
<!DOCTYPE html>
<html lang="en">
<head>
<meta charset="utf-8">
<title>Our Winning 5 Norms – Karvell &amp; Brodick Maritime</title>
<link rel="stylesheet" href="https://fonts.googleapis.com/css2?family=Cinzel:wght@700&family=Cabin+Condensed:wght@600&family=Arimo:wght@400&display=swap">
<style>
  :root {
    --paper: #f7f8f9;
    --paper-edge: #e9ecee;
    --title-blue: #1d95c9;
    --subtitle-grey: #3e5662;
    --ring-blue-light: #63d0f2;
    --ring-blue-dark: #22a6d6;
    --segment-light: #f1f2f3;
    --segment-dark: #c9cdd0;
    --segment-text: #3b4a55;
    --rim: #eef1f3;
  }
  * { margin: 0; padding: 0; box-sizing: border-box; }
  html, body { width: 1200px; height: 1148px; overflow: hidden; }
  body {
    background: radial-gradient(ellipse at 50% 40%, #ffffff 0%, var(--paper) 60%, var(--paper-edge) 100%);
    position: relative;
  }
  .poster-header {
    position: absolute; top: 60px; left: 0; width: 100%;
    text-align: center;
  }
  .poster-title {
    font-family: "Cinzel", serif;
    font-weight: 700;
    color: var(--title-blue);
    font-size: 64px;
    line-height: 1.05;
    letter-spacing: 1px;
  }
  .poster-subtitle {
    margin-top: 34px;
    font-family: "Arimo", sans-serif;
    font-size: 33px;
    color: var(--subtitle-grey);
  }
  .norms-wheel {
    position: absolute; top: 0; left: 0;
  }
  .norm-label {
    font-family: "Cabin Condensed", sans-serif;
    font-weight: 600;
    fill: var(--segment-text);
  }
  .company-name {
    position: absolute; left: 0; bottom: 56px; width: 100%;
    text-align: center;
    font-family: "Arimo", sans-serif;
    font-weight: 400;
    font-size: 28px;
    color: var(--subtitle-grey);
  }
</style>
</head>
<body>
  <header class="poster-header">
    <h1 class="poster-title">Our Winning<br>5 Norms!</h1>
    <p class="poster-subtitle">OWNing the P.A.T.H to Tier 1</p>
  </header>

  <svg class="norms-wheel" width="1200" height="1148" viewBox="0 0 1200 1148" aria-label="Five norms wheel">
    <defs>
      <linearGradient id="ring-fill" x1="0" y1="0" x2="0" y2="1">
        <stop offset="0" stop-color="var(--ring-blue-light)"/>
        <stop offset="1" stop-color="var(--ring-blue-dark)"/>
      </linearGradient>
      <linearGradient id="segment-fill" x1="0" y1="0" x2="0" y2="1">
        <stop offset="0" stop-color="var(--segment-light)"/>
        <stop offset="1" stop-color="var(--segment-dark)"/>
      </linearGradient>
      <linearGradient id="star-fill" x1="0" y1="0" x2="0" y2="1">
        <stop offset="0" stop-color="var(--ring-blue-light)"/>
        <stop offset="1" stop-color="var(--ring-blue-dark)"/>
      </linearGradient>
      <path id="ring-piece" d="M442.1,387.8 A290,290 0 0 1 757.9,387.8 L738.9,417.1 A255,255 0 0 0 461.1,417.1 Z"/>
      <path id="norm-piece" d="M472.5,442 A228,228 0 0 1 727.5,442 L666,533.2 A118,118 0 0 0 534,533.2 Z"/>
      <path id="label-arc" d="M496.6,477.6 A185,185 0 0 1 703.4,477.6"/>
      <path id="label-arc-upper" d="M488.2,465.2 A200,200 0 0 1 711.8,465.2"/>
      <path id="label-arc-lower" d="M506.1,491.7 A168,168 0 0 1 693.9,491.7"/>
    </defs>

    <g class="outer-ring" fill="url(#ring-fill)" stroke="url(#ring-fill)" stroke-width="8" stroke-linejoin="round">
      <use href="#ring-piece" transform="rotate(-6 600 631)"/>
      <use href="#ring-piece" transform="rotate(66 600 631)"/>
      <use href="#ring-piece" transform="rotate(138 600 631)"/>
      <use href="#ring-piece" transform="rotate(210 600 631)"/>
      <use href="#ring-piece" transform="rotate(282 600 631)"/>
    </g>

    <circle class="inner-rim" cx="600" cy="631" r="238" fill="var(--rim)" stroke="#dfe3e6" stroke-width="2"/>

    <g class="norm-segments" fill="url(#segment-fill)" stroke="#ffffff" stroke-width="5" stroke-linejoin="round">
      <g transform="rotate(-36 600 631)">
        <use href="#norm-piece"/>
        <text class="norm-label" font-size="31" stroke="none"><textPath href="#label-arc" startOffset="50%" text-anchor="middle">Ownership</textPath></text>
      </g>
      <g transform="rotate(36 600 631)">
        <use href="#norm-piece"/>
        <text class="norm-label" font-size="29" stroke="none"><textPath href="#label-arc-upper" startOffset="50%" text-anchor="middle">Positive</textPath></text>
        <text class="norm-label" font-size="24" stroke="none"><textPath href="#label-arc-lower" startOffset="50%" text-anchor="middle">Mindset</textPath></text>
      </g>
      <g transform="rotate(108 600 631)">
        <use href="#norm-piece"/>
        <text class="norm-label" font-size="31" stroke="none"><textPath href="#label-arc" startOffset="50%" text-anchor="middle">Actions</textPath></text>
      </g>
      <g transform="rotate(180 600 631)">
        <use href="#norm-piece"/>
        <text class="norm-label" font-size="31" stroke="none"><textPath href="#label-arc" startOffset="50%" text-anchor="middle">Teamwork</textPath></text>
      </g>
      <g transform="rotate(252 600 631)">
        <use href="#norm-piece"/>
        <text class="norm-label" font-size="31" stroke="none"><textPath href="#label-arc" startOffset="50%" text-anchor="middle">Honesty</textPath></text>
      </g>
    </g>

    <polygon class="center-star" fill="url(#star-fill)" stroke="#ffffff" stroke-width="6" stroke-linejoin="round"
      points="600,513 635.3,582.5 712.2,594.5 657.1,649.5 669.4,726.5 600,691 530.6,726.5 542.9,649.5 487.8,594.5 564.7,582.5"/>
  </svg>

  <footer class="company-name">Karvell &amp; Brodick Maritime</footer>
</body>
</html>
```